Startseitenbanner für Onlineshop
Zielgruppe
Wir verkaufen Gurtbänder und Zubehör über den Onlineshop Riemwerk88.de. Für ein neues Design benötigen wir 3 Startseitenbanner. Hier das neue Design im groben Überblick http://kassenhof7.laden-nordstern.de/
Aufgabenstellung
Folgende Banner benötigen wir:
- Reflektorbänder für die Herbst- und Winterzeit (Fotos von Reflektorbändern können wir stellen, allerdings nicht freigestellt). Der Banner soll die Vielfalt des Sortimentes zeigen.
- "Bunte Vielfalt an Bändern". Hier können wir Aufnahmen von Bändern stellen (nicht freigestellt). Wichtig ist es, dass der Kunde eine Übersicht über das Bänderangebot erhält.
- "Banner Privat & Gewerblich": Es wird ein Banner benötigt, der dem Kunden aufzeigt, dass wir an Privatpersonen und Firmen verkaufen. Weiterhin, dass Firmenkunden 5-20% Rabatt erhalten (je nach Jahresumsatz).
Die Umsetzung der Arbeiten sollte umgehend erfolgen.
Daten für die Banner: 1160px x 770px

```html
<!DOCTYPE html>
<html lang="de">
<head>
<meta charset="utf-8">
<title>Riemwerk88.de – Die volle Vielfalt entdecken</title>
<link rel="stylesheet" href="https://fonts.googleapis.com/css2?family=Cabin:wght@400;700&display=swap">
<style>
  :root {
    --stage-bg: #f2f2f2;
    --backdrop: #f4f4f4;
    --tape-blue: #5b7fcf;
    --tape-orange: #ee7a2c;
    --tape-teal: #36b8c2;
    --tape-yellow: #ebc037;
    --tape-brown: #9a5a45;
    --tape-grey: #a9a8a4;
    --tape-white: #ececea;
    --tape-navy: #3e5684;
    --band-orange-dark: #d66d17;
    --band-orange: #ec8d2a;
    --band-orange-light: #f29a35;
    --headline-white: #ffffff;
    --brand-cream: #fbe6cc;
  }
  html, body {
    margin: 0;
    padding: 0;
    width: 1200px;
    height: 797px;
    overflow: hidden;
    background: var(--stage-bg);
  }
  .banner {
    position: relative;
    width: 1200px;
    height: 797px;
    overflow: hidden;
    font-family: "Cabin", "Gill Sans", sans-serif;
  }
  .banner__photo {
    position: absolute;
    left: 0;
    top: 0;
    width: 1200px;
    height: 662px;
    background:
      linear-gradient(180deg, var(--backdrop) 0%, rgba(244,244,244,0.55) 14%, rgba(244,244,244,0) 34%),
      linear-gradient(90deg,
        var(--tape-blue) 0%, var(--tape-orange) 16%, var(--tape-teal) 32%,
        var(--tape-yellow) 42%, var(--tape-brown) 52%, var(--tape-grey) 60%,
        var(--tape-white) 70%, var(--tape-grey) 82%, var(--tape-navy) 100%);
  }
  .banner__band {
    position: absolute;
    left: 0;
    top: 662px;
    width: 1200px;
    height: 135px;
    background: linear-gradient(90deg, var(--band-orange-dark) 0%, var(--band-orange) 45%, var(--band-orange-light) 72%, var(--band-orange) 100%);
  }
  .banner__headline {
    position: absolute;
    left: 47px;
    top: 701px;
    margin: 0;
    color: var(--headline-white);
    font-weight: 700;
    font-size: 46px;
    line-height: 56px;
    letter-spacing: 0.3px;
    text-transform: uppercase;
    white-space: nowrap;
  }
  .banner__brand {
    position: absolute;
    left: 778px;
    top: 703px;
    color: var(--brand-cream);
    font-weight: 400;
    font-size: 40px;
    line-height: 54px;
    letter-spacing: 5px;
    text-transform: uppercase;
    white-space: nowrap;
  }
</style>
</head>
<body>
  <main class="banner">
    <div class="banner__photo" role="img" aria-label="Produktfoto: gestapelte Rollen von Gurtbändern in vielen Farben – Blau, Orange, Türkis, Gelb, Braun, Grau, Weiß mit Streifen, Marine – vor hellem Hintergrund, als Übersicht über das Bänderangebot"></div>
    <div class="banner__band"></div>
    <h1 class="banner__headline">Die volle Vielfalt entdecken</h1>
    <span class="banner__brand">Riemwerk88.de</span>
  </main>
</body>
</html>
```